Black Granite Web Design Project

We are looking for a design for a new company that will be selling Black Granite slabs and tiles. We will be selling to both end-consumers and granite installers. We have already settled on a logo and hopefully this will give an idea of what we like in our designs. We are not going to be selling online but want people to call us so the site is basically an enhanced business card. We will be focusing a lot on SEO so the design will have to keep that in mind.

We would like to keep the design in 1024x768 to make it easily view-able on all devices.

Regarding navigation there should only be a few sub-pages, like "Granite Slabs", "Granite Tiles", "Delivery", "Contact"

Aside from that we are open to designs. One idea we did have was to personalize the site and have a person there somehow to represent the company, making the user feel there are real people behind this site. This is just an idea and not a must.

The name of the company and site is "Silver Brook Petrano"

Thanks
Updates

Hello All,

Thanks for the great designs. There are some good looking designs that show beautiful kitchens but this site is made for the granite installers and not the retail consumers. So in order not to to confuse the buyers I would like to keep this as much about the raw products as possible. The raw products being the granite slabs, thereby making it obvious we don't sell granite counter tops. 

This design will really be the identity of this company so it is important we get the right message across on this index page and that this page is as complete as possible.

Again, thanks for all the work being put into this.

Target Market(s)

The target audience is granite installers or companies that would with granite slabs.

Industry/Entity Type

Business

```html
<!DOCTYPE html>
<html lang="en">
<head>
<meta charset="utf-8">
<title>Silver Brook Petrano – Home</title>
<link href="https://fonts.googleapis.com/css2?family=Saira:wght@500;600;700&family=PT+Sans:wght@400&display=swap" rel="stylesheet">
<style>
  :root {
    --ink: #0a0a0a;
    --white: #ffffff;
    --stone-dark: #2e3d2c;
    --stone-mid: #4d5f48;
    --stone-light: #6f8366;
    --about-bg: #c3c8bd;
    --testi-bg: #a1a79d;
    --nav-edge: #dcdcdc;
    --note-top: #fffff6;
    --note-bottom: #f3f3d6;
    --note-border: #c9cbbd;
    --video-bar: #1b1b1b;
    --video-red: #cc1e1e;
  }
  * { box-sizing: border-box; margin: 0; padding: 0; }
  html, body { width: 1200px; height: 1000px; overflow: hidden; background: var(--white); }
  body { position: relative; font-family: "Saira", sans-serif; color: var(--ink); }

  .sidebar { position: absolute; left: 0; top: 125px; width: 365px; height: 620px; background: var(--white); }
  .brand { position: absolute; left: 24px; top: 30px; width: 320px; text-align: center; }
  .brand-mark { display: block; width: 60px; height: 60px; margin: 0 auto 18px; background: var(--ink); }
  .brand-name { font-weight: 700; font-size: 27px; letter-spacing: -0.5px; line-height: 1; }
  .brand-place { margin-top: 6px; font-weight: 600; font-size: 13px; letter-spacing: 3px; border-top: 1px solid var(--ink); padding-top: 3px; display: inline-block; }

  .main-nav { position: absolute; left: 0; top: 250px; width: 365px; }
  .main-nav a {
    display: block; height: 66px; margin-bottom: 3px; padding-left: 108px; line-height: 64px;
    font-weight: 600; font-size: 21px; color: var(--ink); text-decoration: none;
    background: linear-gradient(#f2f2f2, #fff 30%, #fff 70%, #ececec);
    box-shadow: inset 0 0 6px var(--nav-edge);
  }
  .search { position: absolute; left: 42px; top: 551px; width: 276px; height: 33px; display: flex; border: 2px solid #c8c8c8; border-radius: 3px; background: #ddd; }
  .search-field { flex: 1; margin: 3px 0 3px 3px; background: linear-gradient(#fff, #e9e9e9); border-radius: 2px 0 0 2px; font-family: "PT Sans", sans-serif; font-size: 9px; color: #aaa; line-height: 23px; padding-left: 22px; position: relative; }
  .search-field svg { position: absolute; left: 6px; top: 6px; }
  .search-btn { width: 80px; margin: 3px 3px 3px 0; background: linear-gradient(#8a8a8a, #4a4a4a); color: var(--white); font-size: 12px; font-weight: 600; text-align: center; line-height: 23px; letter-spacing: 0.5px; }

  .stage { position: absolute; left: 365px; top: 125px; width: 635px; height: 620px; background: radial-gradient(ellipse at 55% 45%, var(--stone-light), var(--stone-mid) 55%, var(--stone-dark)); }
  .video { position: absolute; left: 62px; top: 47px; width: 513px; height: 310px; }
  .video-frame { position: absolute; inset: 0 0 24px 0; background: linear-gradient(160deg, #6f8f52 0%, #8a8f80 35%, #6fb4cf 70%, #4e7a3a 100%); }
  .video-play { position: absolute; left: 189px; top: 70px; }
  .video-bar { position: absolute; left: 0; bottom: 0; width: 100%; height: 24px; background: var(--video-bar); color: #ddd; font-family: "PT Sans", sans-serif; font-size: 10px; }
  .video-progress { position: absolute; top: 0; left: 0; width: 100%; height: 3px; background: #555; }
  .video-progress span { display: block; width: 25px; height: 3px; background: var(--video-red); }
  .video-time { position: absolute; left: 72px; top: 7px; }
  .video-time b { color: var(--white); }
  .video-bar svg { position: absolute; top: 6px; }

  .panel { position: absolute; top: 368px; height: 252px; padding: 18px 14px; }
  .panel h2 { font-weight: 600; font-size: 22px; line-height: 1; margin-bottom: 22px; }
  .panel p { font-weight: 500; font-size: 11.5px; line-height: 19px; }
  .about { left: 33px; width: 332px; background: var(--about-bg); }
  .testimonials { left: 378px; width: 226px; background: var(--testi-bg); padding-left: 28px; overflow: hidden; }
  .testimonials h2 { font-size: 20px; }
  .testimonials p + p { margin-top: 19px; }

  .footer { position: absolute; left: 0; top: 745px; width: 1000px; height: 130px; background: var(--ink); color: var(--white); }
  .footer-call { position: absolute; left: 52px; top: 35px; font-weight: 700; line-height: 1; }
  .footer-call span { display: block; font-size: 17px; letter-spacing: 0.3px; }
  .footer-call strong { display: block; font-size: 31px; letter-spacing: 1px; margin-top: 4px; }
  .footer-nav { position: absolute; left: 398px; top: 37px; font-size: 12px; font-weight: 600; }
  .footer-nav a { color: var(--white); text-decoration: none; }
  .footer-nav i { font-style: normal; margin: 0 8px; }
  .copyright { position: absolute; left: 506px; top: 93px; font-size: 8px; font-weight: 600; }
  .footer-brand { position: absolute; left: 769px; top: 0; width: 231px; height: 130px; background: #000; text-align: center; padding-top: 22px; }
  .footer-brand .brand-mark { width: 38px; height: 38px; margin-bottom: 12px; background: var(--white); }
  .footer-brand .brand-name { font-size: 17px; }
  .footer-brand .brand-place { font-size: 8px; letter-spacing: 2px; border-top-color: var(--white); }

  .note { position: absolute; left: 977px; top: 151px; width: 212px; height: 371px; border: 2px solid var(--note-border); border-radius: 10px; background: linear-gradient(var(--note-top), var(--note-bottom)); padding: 28px 0 0 13px; font-family: "PT Sans", sans-serif; font-size: 21px; line-height: 29.2px; color: var(--ink); white-space: nowrap; }
</style>
</head>
<body>
  <aside class="sidebar">
    <div class="brand">
      <span class="brand-mark"></span>
      <div class="brand-name">SILVER BROOK PETRANO</div>
      <div class="brand-place">CEDAR HOLLOW</div>
    </div>
    <nav class="main-nav">
      <a href="#">Granite Slabs</a>
      <a href="#">Granite Tiles</a>
      <a href="#">Delivery</a>
      <a href="#">Contact</a>
    </nav>
    <div class="search">
      <div class="search-field">
        <svg width="11" height="11" viewBox="0 0 11 11"><circle cx="4.5" cy="4.5" r="3.5" fill="none" stroke="#999" stroke-width="1.4"/><line x1="7" y1="7" x2="10.5" y2="10.5" stroke="#999" stroke-width="1.6"/></svg>
        Search Keyword...
      </div>
      <div class="search-btn">SEARCH</div>
    </div>
  </aside>

  <main class="stage" role="img" aria-label="Dark green polished granite tile background">
    <div class="video">
      <div class="video-frame" role="img" aria-label="Video still of the owner talking beside a backyard pool"></div>
      <svg class="video-play" width="112" height="112" viewBox="0 0 112 112"><circle cx="56" cy="56" r="53" fill="none" stroke="#fff" stroke-width="4"/><polygon points="44,32 44,80 82,56" fill="#fff"/></svg>
      <div class="video-bar">
        <div class="video-progress"><span></span></div>
        <svg style="left:16px" width="12" height="12" viewBox="0 0 12 12"><polygon points="1,0 1,12 11,6" fill="#bbb"/></svg>
        <svg style="left:46px" width="14" height="12" viewBox="0 0 14 12"><polygon points="0,4 3,4 7,0 7,12 3,8 0,8" fill="#bbb"/><path d="M9 3 Q12 6 9 9" stroke="#bbb" fill="none"/></svg>
        <span class="video-time"><b>00:25</b> / 10:41</span>
        <svg style="left:464px" width="14" height="12" viewBox="0 0 14 12"><rect x="1" y="2" width="12" height="8" fill="none" stroke="#fff" stroke-width="2"/></svg>
        <svg style="left:490px" width="14" height="12" viewBox="0 0 14 12"><path d="M1 4V1h3M10 1h3v3M13 8v3h-3M4 11H1V8" stroke="#bbb" fill="none" stroke-width="1.5"/></svg>
      </div>
    </div>

    <section class="panel about">
      <h2>About Silver Brook Petrano</h2>
      <p>We cut, grade and ship raw black granite slabs and tiles straight from our own quarry partners. Every slab is checked by hand for colour, depth and polish before it leaves the yard, so installers know what they get. We do not make bench tops; we supply the stone that the best fitters in the trade rely on. Call our team and we will help you pick the right slab for your next job.</p>
    </section>
    <section class="panel testimonials">
      <h2>Testimonials</h2>
      <p>“Great slabs, even colour and always on time. The team knows stone and makes ordering simple for our crew.”</p>
      <p>“Clean cuts, solid polish and fair prices. We have used them on every job this year and will keep on</p>
    </section>
  </main>

  <footer class="footer">
    <div class="footer-call"><span>CALL TODAY FOR A QUOTE</span><strong>1300 555 019</strong></div>
    <nav class="footer-nav">
      <a href="#">Granite Slabs</a><i>|</i><a href="#">Granite Tiles</a><i>|</i><a href="#">Delivery</a><i>|</i><a href="#">Contact</a>
    </nav>
    <div class="copyright">Copyright © Silver Brook Petrano</div>
    <div class="footer-brand">
      <span class="brand-mark"></span>
      <div class="brand-name">SILVER BROOK PETRANO</div>
      <div class="brand-place">CEDAR HOLLOW</div>
    </div>
  </footer>

  <div class="note">A video on the<br>Home page<br>would help give a<br>personal touch<br>about the<br>business &amp;<br>you can reinforce<br>to ‘call for a quote’<br>if this is your<br>preferred method<br>of contact</div>
</body>
</html>
```